RM BIZ CARDS

Hi,

Is it possible to see a one sided version (with logo and info) as well as a two-sided version (front side w/logo and back side with info)?
How do we choose card stock and finish once we approve a design?

We would like the following info included:

Peter Lowell
Rosfeld Talent Media
4127 Marwick Lane, Suite 300
Los Angeles, CA 90041
(323) 555-0148
peter@rosfeldtalentmedia.example

```html
<!DOCTYPE html>
<html lang="en">
<head>
<meta charset="utf-8">
<title>Rosfeld Talent Media – Business Card</title>
<link href="https://fonts.googleapis.com/css2?family=Roboto:wght@300;400&display=swap" rel="stylesheet">
<style>
  :root {
    --canvas: #e6e4e0;
    --ink: #1f1f1f;
    --ink-soft: #5a5a5a;
    --card-white: #ffffff;
    --card-white-shade: #ececec;
    --card-black: #0d0d0d;
    --card-black-lift: #3a3a3a;
    --on-black: #f4f4f4;
  }
  * { margin: 0; padding: 0; box-sizing: border-box; }
  html, body {
    width: 1200px; height: 1023px; overflow: hidden;
    background: var(--canvas);
    font-family: "Roboto", Arial, sans-serif;
  }
  .card {
    position: absolute; left: 150px; top: 254px;
    width: 900px; height: 514px;
    border-radius: 22px; overflow: hidden;
    background: linear-gradient(160deg, var(--card-white) 40%, var(--card-white-shade) 100%);
    box-shadow: 0 18px 40px rgba(0,0,0,.22), 0 2px 6px rgba(0,0,0,.12);
  }
  .brand-panel {
    position: absolute; left: 0; top: 0;
    width: 360px; height: 100%;
    background: radial-gradient(ellipse at 55% 45%, var(--card-black-lift) 0%, var(--card-black) 70%);
  }
  .brand-notch {
    position: absolute; left: 358px; top: 128px;
    width: 26px; height: 44px;
  }
  .brand-mark {
    position: absolute; left: 150px; top: 190px;
    width: 60px; height: 60px;
    border: 3px solid var(--on-black); border-radius: 50%;
  }
  .brand-name {
    position: absolute; left: 0; top: 290px; width: 360px;
    text-align: center;
    color: var(--on-black);
    font-weight: 300; font-size: 31px; letter-spacing: 2px;
  }
  .contact {
    position: absolute; left: 412px; top: 118px;
    color: var(--ink);
  }
  .contact-name {
    font-weight: 300; font-size: 44px; letter-spacing: 1px;
    text-transform: uppercase; line-height: 1;
  }
  .contact-role {
    margin-top: 12px;
    font-weight: 300; font-size: 19px; color: var(--ink-soft);
  }
  .contact-address {
    margin-top: 30px;
    font-weight: 300; font-size: 22px; line-height: 1.45; color: var(--ink-soft);
  }
  .contact-lines { margin-top: 26px; list-style: none; }
  .contact-lines li {
    display: flex; align-items: center; gap: 12px;
    font-weight: 300; font-size: 22px; line-height: 1.5; color: var(--ink-soft);
  }
  .contact-lines svg { width: 16px; height: 16px; flex: none; }
</style>
</head>
<body>
  <div class="card">
    <div class="brand-panel">
      <span class="brand-mark" aria-hidden="true"></span>
      <div class="brand-name">ROSFELD TALENT</div>
    </div>
    <svg class="brand-notch" viewBox="0 0 26 44" aria-hidden="true">
      <polygon points="0,0 24,22 0,44" fill="#161616"/>
    </svg>
    <div class="contact">
      <div class="contact-name">Peter Lowell</div>
      <div class="contact-role">Director</div>
      <div class="contact-address">
        4127 Marwick Lane, Suite 300<br>
        Los Angeles, CA 90041
      </div>
      <ul class="contact-lines">
        <li>
          <svg viewBox="0 0 16 16" aria-hidden="true"><path d="M3.5 1.5l2.5 0 1 3.5-1.6 1.2a8 8 0 0 0 4.4 4.4L11 9l3.5 1v2.5c0 1-.8 1.8-1.8 1.7C7 13.7 2.3 9 1.8 3.3 1.7 2.3 2.5 1.5 3.5 1.5z" fill="#333"/></svg>
          (323) 555-0148
        </li>
        <li>
          <svg viewBox="0 0 16 16" aria-hidden="true"><rect x="1.5" y="3.5" width="13" height="9" fill="none" stroke="#333" stroke-width="1.4"/><path d="M1.5 3.5L8 9l6.5-5.5" fill="none" stroke="#333" stroke-width="1.4"/></svg>
          peter@rosfeldtalentmedia.example
        </li>
      </ul>
    </div>
  </div>
</body>
</html>
```